Plakat-Design für Softwareentwicklung
Zielgruppe
Gemeinsam mit den Kunden entwickelt Velmoria hochkomplexe, sicherheitskritische Komponenten im Bereich der Softwareentwicklung für Automotive, Medical, Avionik-, und Defence, sowie Industriesysteme, nach branchenüblichen Vorgehensmodellen und Vorgaben (https://www.velmoria-beispiel.de/).
Wir suchen ein Design für unsere Kalenderplakate für das Jahr 2019.
Die Kalenderplakate benötigen wir für unsere internen Mitarbeiter und Geschäftskunden/-partner (B2B).
Aufgabenstellung
In den letzten Jahren haben wir das Kalenderplakat sowohl in DIN A3 und DIN B1 anfertigen lassen.
Das Kalenderplakat sollte praktisch und optisch ansprechend gestaltet sein, sodass man es sich gerne als Jahresplaner in sein Büro hängt. Welche Bilder/Fotos Sie nutzen, welches Design Sie wählen, bleibt komplett Ihnen überlassen. Wir möchten hier Ihre Kreativität nicht einschränken.
Neben dem Kalender (Tage nach Monaten sortiert, die letzten beiden Monate von 2018 und die ersten beiden von 2020 bitte ebenfalls integrieren, Wochenende und Feiertage farblich hervorheben), sollten auch unsere Kontaktdaten und unser Logo auf dem Plakat abgebildet werden.
Unser Slogan lautet 'Engineering with Precision'.
Wir freuen uns auf Ihre Vorschläge!

```html
<!DOCTYPE html>
<html lang="de">
<head>
<meta charset="utf-8">
<title>Velmoria Kalender 2019</title>
<link href="https://fonts.googleapis.com/css2?family=Oswald:wght@400;500&family=Roboto+Condensed:wght@400;700&display=swap" rel="stylesheet">
<style>
  :root{
    --bg:#ececec;
    --paper:#ffffff;
    --slate:#48474a;
    --green:#3f9c80;
    --red:#d2232a;
    --ink:#2e2e30;
    --muted:#8a8a8c;
    --footer-text:#e6e6e6;
  }
  *{box-sizing:border-box;margin:0;padding:0}
  html,body{width:1200px;height:900px;overflow:hidden;background:var(--bg)}
  body{font-family:"Roboto Condensed",Arial,sans-serif;color:var(--ink)}

  .poster{position:absolute;left:295px;top:20px;width:610px;height:860px;background:var(--paper);box-shadow:0 6px 18px rgba(0,0,0,.18)}

  .sidebar{position:absolute;left:0;top:0;width:240px;height:100%;display:flex;flex-direction:column}
  .brand{height:100px;background:var(--slate);padding:36px 0 0 26px}
  .brand-name{font-family:"Oswald",sans-serif;font-weight:400;font-size:26px;line-height:1;color:#8fb3a8;letter-spacing:.3px}
  .brand-slogan{font-size:8px;color:#9a999c;margin-top:4px;letter-spacing:.2px}
  .photo{flex:1;background:
      radial-gradient(ellipse 120% 60% at 100% 45%, #2f4a4a 0%, #49676a 30%, rgba(0,0,0,0) 55%),
      radial-gradient(ellipse 90% 50% at 0% 30%, #d8d4a6 0%, #a8a77a 35%, rgba(0,0,0,0) 70%),
      linear-gradient(170deg,#5f6e5a 0%,#8f9872 30%,#3e5657 60%,#7d8b6f 80%,#2e3a37 100%)}
  .contact{height:110px;background:var(--slate);padding:14px 16px 0 20px;display:flex;flex-direction:column;gap:6px}
  .contact-row{display:flex;align-items:flex-start;gap:10px;font-size:7.5px;line-height:1.3;color:var(--footer-text)}
  .contact-row svg{flex:0 0 12px;width:12px;height:12px;fill:none;stroke:var(--footer-text);stroke-width:1.4}
  .contact-row strong{font-weight:700}
  .contact-row .sep{color:var(--green)}

  .title-box{position:absolute;left:240px;top:16px;width:255px;height:84px;background:var(--slate);box-shadow:4px 4px 0 var(--green);text-align:center;padding-top:13px;font-family:"Oswald",sans-serif}
  .title-year{color:var(--green);font-size:23px;line-height:1;font-weight:500}
  .title-word{color:#fff;font-size:25px;line-height:1.1;font-weight:500;letter-spacing:2.5px}

  .calendar{position:absolute;left:254px;top:112px;width:336px;display:grid;grid-template-columns:repeat(3,112px);row-gap:10px}
  .month{padding:0 6px}
  .month.start-col2{grid-column:2}
  .month.start-col1{grid-column:1}
  .month h3{font-family:"Oswald",sans-serif;font-weight:400;font-size:8px;color:var(--green);text-align:center;letter-spacing:.5px;line-height:11px}
  .weekdays,.days{display:grid;grid-template-columns:repeat(7,1fr);text-align:center}
  .weekdays{font-size:4.6px;color:var(--muted);line-height:9px;text-transform:uppercase}
  .days{font-size:6.2px;line-height:15px;color:var(--ink);height:90px;align-content:start}
  .days > :nth-child(7n+6),.days > :nth-child(7n){color:var(--red)}
  .days .holiday{color:var(--red)}
</style>
</head>
<body>
<main class="poster">
  <aside class="sidebar">
    <header class="brand">
      <div class="brand-name">Velmoria</div>
      <div class="brand-slogan">Engineering with Precision</div>
    </header>
    <div class="photo" role="img" aria-label="Abstrakte Langzeitbelichtung mit geschwungenen Lichtbögen in Sandgelb und Petrol"></div>
    <footer class="contact">
      <div class="contact-row">
        <svg viewBox="0 0 12 12"><path d="M6 11C3.5 8 2.5 6.3 2.5 4.5a3.5 3.5 0 0 1 7 0C9.5 6.3 8.5 8 6 11z"/><circle cx="6" cy="4.5" r="1.2"/></svg>
        <span><strong>HEADQUARTER</strong> <span class="sep">//</span> Lindenauer Str. 14b, 80999 Munich<br>Germany</span>
      </div>
      <div class="contact-row">
        <svg viewBox="0 0 12 12"><path d="M3 1.5l2 2.3-1.1 1.3a7 7 0 0 0 3 3l1.3-1.1 2.3 2-1.3 1.5C5.5 10.5 1.5 6.5 1.5 2.8z"/></svg>
        <span><strong>PHONE</strong> <span class="sep">//</span> +49 89 000420 - 0<br><strong>FAX</strong> <span class="sep">//</span> +49 89 000420-99</span>
      </div>
      <div class="contact-row">
        <svg viewBox="0 0 12 12"><rect x="1" y="2.5" width="10" height="7"/><path d="M1 2.5l5 4 5-4"/></svg>
        <span>info@velmoria-beispiel.de</span>
      </div>
      <div class="contact-row">
        <svg viewBox="0 0 12 12"><circle cx="6" cy="6" r="4.8"/><ellipse cx="6" cy="6" rx="2" ry="4.8"/><path d="M1.2 6h9.6"/></svg>
        <span>www.velmoria-beispiel.de</span>
      </div>
    </footer>
  </aside>

  <div class="title-box">
    <div class="title-year">2019</div>
    <div class="title-word">KALENDER</div>
  </div>

  <section class="calendar">
    <article class="month start-col2"><h3>NOVEMBER</h3>
      <div class="weekdays"><span>Mo</span><span>Di</span><span>Mi</span><span>Do</span><span>Fr</span><span>Sa</span><span>So</span></div>
      <div class="days"><i></i><i></i><i></i><span class="holiday">1</span><span>2</span><span>3</span><span>4</span><span>5</span><span>6</span><span>7</span><span>8</span><span>9</span><span>10</span><span>11</span><span>12</span><span>13</span><span>14</span><span>15</span><span>16</span><span>17</span><span>18</span><span>19</span><span>20</span><span>21</span><span>22</span><span>23</span><span>24</span><span>25</span><span>26</span><span>27</span><span>28</span><span>29</span><span>30</span></div>
    </article>
    <article class="month"><h3>DEZEMBER</h3>
      <div class="weekdays"><span>Mo</span><span>Di</span><span>Mi</span><span>Do</span><span>Fr</span><span>Sa</span><span>So</span></div>
      <div class="days"><i></i><i></i><i></i><i></i><i></i><span>1</span><span>2</span><span>3</span><span>4</span><span>5</span><span>6</span><span>7</span><span>8</span><span>9</span><span>10</span><span>11</span><span>12</span><span>13</span><span>14</span><span>15</span><span>16</span><span>17</span><span>18</span><span>19</span><span>20</span><span>21</span><span>22</span><span>23</span><span>24</span><span class="holiday">25</span><span class="holiday">26</span><span>27</span><span>28</span><span>29</span><span>30</span><span>31</span></div>
    </article>

    <article class="month start-col1"><h3>JANUAR</h3>
      <div class="weekdays"><span>Mo</span><span>Di</span><span>Mi</span><span>Do</span><span>Fr</span><span>Sa</span><span>So</span></div>
      <div class="days"><i></i><span class="holiday">1</span><span>2</span><span>3</span><span>4</span><span>5</span><span>6</span><span>7</span><span>8</span><span>9</span><span>10</span><span>11</span><span>12</span><span>13</span><span>14</span><span>15</span><span>16</span><span>17</span><span>18</span><span>19</span><span>20</span><span>21</span><span>22</span><span>23</span><span>24</span><span>25</span><span>26</span><span>27</span><span>28</span><span>29</span><span>30</span><span>31</span></div>
    </article>
    <article class="month"><h3>FEBRUAR</h3>
      <div class="weekdays"><span>Mo</span><span>Di</span><span>Mi</span><span>Do</span><span>Fr</span><span>Sa</span><span>So</span></div>
      <div class="days"><i></i><i></i><i></i><i></i><span>1</span><span>2</span><span>3</span><span>4</span><span>5</span><span>6</span><span>7</span><span>8</span><span>9</span><span>10</span><span>11</span><span>12</span><span>13</span><span>14</span><span>15</span><span>16</span><span>17</span><span>18</span><span>19</span><span>20</span><span>21</span><span>22</span><span>23</span><span>24</span><span>25</span><span>26</span><span>27</span><span>28</span></div>
    </article>
    <article class="month"><h3>MÄRZ</h3>
      <div class="weekdays"><span>Mo</span><span>Di</span><span>Mi</span><span>Do</span><span>Fr</span><span>Sa</span><span>So</span></div>
      <div class="days"><i></i><i></i><i></i><i></i><span>1</span><span>2</span><span>3</span><span>4</span><span>5</span><span>6</span><span>7</span><span>8</span><span>9</span><span>10</span><span>11</span><span>12</span><span>13</span><span>14</span><span>15</span><span>16</span><span>17</span><span>18</span><span>19</span><span>20</span><span>21</span><span>22</span><span>23</span><span>24</span><span>25</span><span>26</span><span>27</span><span>28</span><span>29</span><span>30</span><span>31</span></div>
    </article>

    <article class="month"><h3>APRIL</h3>
      <div class="weekdays"><span>Mo</span><span>Di</span><span>Mi</span><span>Do</span><span>Fr</span><span>Sa</span><span>So</span></div>
      <div class="days"><span>1</span><span>2</span><span>3</span><span>4</span><span>5</span><span>6</span><span>7</span><span>8</span><span>9</span><span>10</span><span>11</span><span>12</span><span>13</span><span>14</span><span>15</span><span>16</span><span>17</span><span>18</span><span class="holiday">19</span><span>20</span><span>21</span><span class="holiday">22</span><span>23</span><span>24</span><span>25</span><span>26</span><span>27</span><span>28</span><span>29</span><span>30</span></div>
    </article>
    <article class="month"><h3>MAI</h3>
      <div class="weekdays"><span>Mo</span><span>Di</span><span>Mi</span><span>Do</span><span>Fr</span><span>Sa</span><span>So</span></div>
      <div class="days"><i></i><i></i><span class="holiday">1</span><span>2</span><span>3</span><span>4</span><span>5</span><span>6</span><span>7</span><span>8</span><span>9</span><span>10</span><span>11</span><span>12</span><span>13</span><span>14</span><span>15</span><span>16</span><span>17</span><span>18</span><span>19</span><span>20</span><span>21</span><span>22</span><span>23</span><span>24</span><span>25</span><span>26</span><span>27</span><span>28</span><span>29</span><span class="holiday">30</span><span>31</span></div>
    </article>
    <article class="month"><h3>JUNI</h3>
      <div class="weekdays"><span>Mo</span><span>Di</span><span>Mi</span><span>Do</span><span>Fr</span><span>Sa</span><span>So</span></div>
      <div class="days"><i></i><i></i><i></i><i></i><i></i><span>1</span><span>2</span><span>3</span><span>4</span><span>5</span><span>6</span><span>7</span><span>8</span><span>9</span><span class="holiday">10</span><span>11</span><span>12</span><span>13</span><span>14</span><span>15</span><span>16</span><span>17</span><span>18</span><span>19</span><span class="holiday">20</span><span>21</span><span>22</span><span>23</span><span>24</span><span>25</span><span>26</span><span>27</span><span>28</span><span>29</span><span>30</span></div>
    </article>

    <article class="month"><h3>JULI</h3>
      <div class="weekdays"><span>Mo</span><span>Di</span><span>Mi</span><span>Do</span><span>Fr</span><span>Sa</span><span>So</span></div>
      <div class="days"><span>1</span><span>2</span><span>3</span><span>4</span><span>5</span><span>6</span><span>7</span><span>8</span><span>9</span><span>10</span><span>11</span><span>12</span><span>13</span><span>14</span><span>15</span><span>16</span><span>17</span><span>18</span><span>19</span><span>20</span><span>21</span><span>22</span><span>23</span><span>24</span><span>25</span><span>26</span><span>27</span><span>28</span><span>29</span><span>30</span><span>31</span></div>
    </article>
    <article class="month"><h3>AUGUST</h3>
      <div class="weekdays"><span>Mo</span><span>Di</span><span>Mi</span><span>Do</span><span>Fr</span><span>Sa</span><span>So</span></div>
      <div class="days"><i></i><i></i><i></i><span>1</span><span>2</span><span>3</span><span>4</span><span>5</span><span>6</span><span>7</span><span>8</span><span>9</span><span>10</span><span>11</span><span>12</span><span>13</span><span>14</span><span class="holiday">15</span><span>16</span><span>17</span><span>18</span><span>19</span><span>20</span><span>21</span><span>22</span><span>23</span><span>24</span><span>25</span><span>26</span><span>27</span><span>28</span><span>29</span><span>30</span><span>31</span></div>
    </article>
    <article class="month"><h3>SEPTEMBER</h3>
      <div class="weekdays"><span>Mo</span><span>Di</span><span>Mi</span><span>Do</span><span>Fr</span><span>Sa</span><span>So</span></div>
      <div class="days"><i></i><i></i><i></i><i></i><i></i><i></i><span>1</span><span>2</span><span>3</span><span>4</span><span>5</span><span>6</span><span>7</span><span>8</span><span>9</span><span>10</span><span>11</span><span>12</span><span>13</span><span>14</span><span>15</span><span>16</span><span>17</span><span>18</span><span>19</span><span>20</span><span>21</span><span>22</span><span>23</span><span>24</span><span>25</span><span>26</span><span>27</span><span>28</span><span>29</span><span>30</span></div>
    </article>

    <article class="month"><h3>OKTOBER</h3>
      <div class="weekdays"><span>Mo</span><span>Di</span><span>Mi</span><span>Do</span><span>Fr</span><span>Sa</span><span>So</span></div>
      <div class="days"><i></i><span>1</span><span>2</span><span class="holiday">3</span><span>4</span><span>5</span><span>6</span><span>7</span><span>8</span><span>9</span><span>10</span><span>11</span><span>12</span><span>13</span><span>14</span><span>15</span><span>16</span><span>17</span><span>18</span><span>19</span><span>20</span><span>21</span><span>22</span><span>23</span><span>24</span><span>25</span><span>26</span><span>27</span><span>28</span><span>29</span><span>30</span><span>31</span></div>
    </article>
    <article class="month"><h3>NOVEMBER</h3>
      <div class="weekdays"><span>Mo</span><span>Di</span><span>Mi</span><span>Do</span><span>Fr</span><span>Sa</span><span>So</span></div>
      <div class="days"><i></i><i></i><i></i><i></i><span class="holiday">1</span><span>2</span><span>3</span><span>4</span><span>5</span><span>6</span><span>7</span><span>8</span><span>9</span><span>10</span><span>11</span><span>12</span><span>13</span><span>14</span><span>15</span><span>16</span><span>17</span><span>18</span><span>19</span><span>20</span><span>21</span><span>22</span><span>23</span><span>24</span><span>25</span><span>26</span><span>27</span><span>28</span><span>29</span><span>30</span></div>
    </article>
    <article class="month"><h3>DEZEMBER</h3>
      <div class="weekdays"><span>Mo</span><span>Di</span><span>Mi</span><span>Do</span><span>Fr</span><span>Sa</span><span>So</span></div>
      <div class="days"><i></i><i></i><i></i><i></i><i></i><i></i><span>1</span><span>2</span><span>3</span><span>4</span><span>5</span><span>6</span><span>7</span><span>8</span><span>9</span><span>10</span><span>11</span><span>12</span><span>13</span><span>14</span><span>15</span><span>16</span><span>17</span><span>18</span><span>19</span><span>20</span><span>21</span><span>22</span><span>23</span><span>24</span><span class="holiday">25</span><span class="holiday">26</span><span>27</span><span>28</span><span>29</span><span>30</span><span>31</span></div>
    </article>

    <article class="month"><h3>JANUAR</h3>
      <div class="weekdays"><span>Mo</span><span>Di</span><span>Mi</span><span>Do</span><span>Fr</span><span>Sa</span><span>So</span></div>
      <div class="days"><i></i><i></i><span class="holiday">1</span><span>2</span><span>3</span><span>4</span><span>5</span><span class="holiday">6</span><span>7</span><span>8</span><span>9</span><span>10</span><span>11</span><span>12</span><span>13</span><span>14</span><span>15</span><span>16</span><span>17</span><span>18</span><span>19</span><span>20</span><span>21</span><span>22</span><span>23</span><span>24</span><span>25</span><span>26</span><span>27</span><span>28</span><span>29</span><span>30</span><span>31</span></div>
    </article>
    <article class="month"><h3>FEBRUAR</h3>
      <div class="weekdays"><span>Mo</span><span>Di</span><span>Mi</span><span>Do</span><span>Fr</span><span>Sa</span><span>So</span></div>
      <div class="days"><i></i><i></i><i></i><i></i><i></i><span>1</span><span>2</span><span>3</span><span>4</span><span>5</span><span>6</span><span>7</span><span>8</span><span>9</span><span>10</span><span>11</span><span>12</span><span>13</span><span>14</span><span>15</span><span>16</span><span>17</span><span>18</span><span>19</span><span>20</span><span>21</span><span>22</span><span>23</span><span>24</span><span>25</span><span>26</span><span>27</span><span>28</span><span>29</span></div>
    </article>
  </section>
</main>
</body>
</html>
```